Visitenkarten-Design für ein Juwelier Geschäft
Zielgruppe
Juwelier Geschäft in modernem offenen design.
Zielgruppe sind kunden und partner/marken
Aufgabenstellung
schlichtes edles Design.
karten sollen später geprägt werden und einen goldschnitt erhalten

```html
<!DOCTYPE html>
<html lang="de">
<head>
<meta charset="utf-8">
<title>Juwelier Veldhoven – Visitenkarte</title>
<link href="https://fonts.googleapis.com/css2?family=Lato:wght@300;400;700;900&display=swap" rel="stylesheet">
<style>
  :root {
    --backdrop: #c18f58;
    --card-white: #ffffff;
    --frame-gold: #f2d22e;
    --ink: #111111;
    --ink-soft: #2a2a2a;
    --logo-faint: rgba(190, 205, 210, 0.85);
    --photo-cool: #c9d0cf;
    --photo-peach: #e7ab6e;
    --photo-skin: #efc9b4;
    --photo-wash: #f1f1f1;
  }
  * { margin: 0; padding: 0; box-sizing: border-box; }
  html, body {
    width: 1200px; height: 1200px; overflow: hidden;
    background: var(--backdrop);
    font-family: "Lato", Arial, sans-serif;
  }
  .stage { position: relative; width: 1200px; height: 1200px; }
  .card {
    position: absolute; left: 260px; width: 680px; height: 440px;
    overflow: hidden; background: var(--card-white);
  }
  .card--front { top: 117px; }
  .card--back { top: 648px; }

  .card__photo {
    position: absolute; inset: 0;
    background:
      radial-gradient(ellipse 38% 60% at 62% 45%, var(--photo-skin) 0%, rgba(239,201,180,0) 100%),
      linear-gradient(100deg, var(--photo-cool) 0%, var(--photo-peach) 32%, #f0c2a4 55%, var(--photo-skin) 70%, #d9b39a 88%, var(--photo-cool) 100%);
  }
  .card__photo--washed {
    background: linear-gradient(100deg, #eceeee 0%, var(--photo-wash) 40%, #f6f3f1 70%, #eceeee 100%);
  }
  .card__frame {
    position: absolute; left: 39px; top: 42px; width: 602px; height: 356px;
    border: 1.5px solid var(--frame-gold);
  }
  .card--front .card__frame { background: rgba(231, 160, 90, 0.22); }
  .card--back .card__frame { background: var(--card-white); }

  .brand-mark { position: absolute; left: 57px; top: 55px; color: var(--logo-faint); }
  .brand-mark__kind { font-weight: 300; font-size: 15px; letter-spacing: 0.5px; line-height: 1; }
  .brand-mark__name { font-weight: 900; font-size: 26px; letter-spacing: 0.5px; line-height: 1.1; }

  .contact {
    position: absolute; right: 31px; top: 22px; text-align: right; color: var(--ink-soft);
  }
  .contact__name {
    font-weight: 700; font-size: 28px; letter-spacing: 2px; color: var(--ink); line-height: 1.2;
    margin-bottom: 3px;
  }
  .contact__line { font-weight: 300; font-size: 20px; line-height: 31px; }

  .brand { position: absolute; left: 25px; bottom: 8px; color: var(--ink); }
  .brand__kind { font-weight: 300; font-size: 39px; line-height: 1; letter-spacing: 0.5px; }
  .brand__name { font-weight: 900; font-size: 64px; line-height: 1; letter-spacing: 1px; margin-top: 6px; }
</style>
</head>
<body>
<main class="stage">
  <section class="card card--front">
    <div class="card__photo" role="img" aria-label="Porträtfoto einer Frau mit goldenem Ohrhänger vor warmem orangefarbenem Stoff"></div>
    <div class="card__frame"></div>
    <div class="brand-mark">
      <p class="brand-mark__kind">JUWELIER</p>
      <p class="brand-mark__name">VELDHOVEN</p>
    </div>
  </section>

  <section class="card card--back">
    <div class="card__photo card__photo--washed" role="img" aria-label="Stark aufgehelltes Porträtfoto als Hintergrund"></div>
    <div class="card__frame">
      <div class="contact">
        <p class="contact__name">LENA BEISPIEL</p>
        <p class="contact__line">kontakt@veldhoven-post.de</p>
        <p class="contact__line">0123 9876540</p>
      </div>
      <div class="brand">
        <p class="brand__kind">JUWELIER</p>
        <p class="brand__name">VELDHOVEN</p>
      </div>
    </div>
  </section>
</main>
</body>
</html>
```